Poster for teenagers

Bright, trendy, modern and young fonts - a variety of fonts, plus arrows and clip art (no photos) for an A3 size poster to be hung in study halls of schools. There are six dot points. I think each point should be in some kind of box or circle.

Here are a few ideas of the kind of thing I mean.
http://www.varrowdale.example.gov.au/Page/Images/youth_Advisory_Group_Poster_(1).jpg

http://www.brindlecourt.example/sites/default/files/Youth-Panel-Poster-1-Web.jpg

http://www.quillmarsh.example.org.au/images/librariesprovider4/Misc-illustrations/140335-qui-youth-superheros-heroup-highres.jpg?sfvrsn=0

https://pkrvworldwide.files.examplehost.com/2013/04/544477_432153653542694_970534114_n.jpg

Also my logo should be on it some where . I've attached a my logo.

Here is the text:
How to get organised and motivated this year.
1. Write stuff down
Write down things you need to do and when you plan to do them. Use digital calendars, to do apps and email lists – or pen and paper. Even if you are sure you will remember – get it out of your head and onto paper/your phone/laptop. You are more likely to get it done and feel less stressed.
2. Set up habits
If you do things in the same way, at the same time or after the same thing – then after a few weeks, it becomes much easier to get those things done. Set up a particular time, or place to do study tasks – or link them with another daily task. EG: art homework every Tuesday. Violin practice after breakfast.
3. Focus!
For 15-30 minutes at a time - totally focus on homework. Put your phone away, log out of chatterloop, close down other programs and really concentrate. Then have a break, send a text or whatever – and then go back to focussed study. Fifteen minutes of concentrated study gets more achieved than an hour of study switching back and forth between homework and other activities.
4. Just do something
No motivation? Just take a “bite”. Set a timer and just do 5 minutes. Or 15. Or read just the first two pages. Or the first problem on the worksheet. Something is better than nothing – and sometimes once you start, it’s easier to keep going.
5. Use rewards and consequences
Reward yourself when you do a hard task and use consequences when you don’t. Use food, fun activities, gaming and social time to motivate yourself – you get it when you do tasks, you don’t when you don’t. EG 15 minutes of clipstream when I finish this page. Tell other people your plans and you are more likely to stick to them.
6. Imagine the future
When you really can’t be find any motivation to do the things you need to do – take 30 seconds to think about what will happen in a week, month and year if you get on with it. What will happen then and how will that feel. And imagine what will happen in a week, month and year if you DON’T do those things – and how will that feel.

Good luck !
For free articles and one to one help with study skills, increasing motivation, coping with stress or tough times in senior school, go to tallowbrook.example.net.au
Tallow Brook Psychology and Education

```html
<!DOCTYPE html>
<html lang="en">
<head>
<meta charset="utf-8">
<title>How to Get Organised and Motivated This Year</title>
<link rel="stylesheet" href="https://fonts.googleapis.com/css2?family=Fredoka:wght@500;600&family=Tinos:wght@400;700&display=swap">
<style>
  :root {
    --page: #ffffff;
    --red: #cf2027;
    --orange: #e2562a;
    --amber: #f0a93a;
    --yellow: #f3c744;
    --lime: #93c13e;
    --green: #3f8c3b;
    --cyan: #1b9ad7;
    --navy: #2e2a7c;
    --purple: #7b2b84;
    --violet: #5d2d8c;
    --c-title: #8fbf3f;
    --c-one: #1a9ad6;
    --c-two: #2e2a7a;
    --c-three: #7a2a84;
    --c-four: #3e8a3a;
    --c-five: #d24f28;
    --c-six: #c61f29;
    --c-luck: #8fbf3f;
    --ink-light: #ffffff;
    --footer-ink: #6e5a2c;
    --brand-ink: #5b7d2c;
  }
  * { box-sizing: border-box; margin: 0; padding: 0; }
  html, body { width: 1200px; height: 1000px; overflow: hidden; background: var(--page); }
  .poster {
    position: absolute; left: 283px; top: 50px; width: 639px; height: 908px;
    background: var(--page); overflow: hidden;
  }
  .field {
    position: absolute; left: 0; top: 0; width: 639px; height: 808px; overflow: hidden;
    background: repeating-linear-gradient(90deg,
      var(--red) 0 18px, var(--orange) 18px 36px, var(--amber) 36px 54px,
      var(--lime) 54px 72px, var(--green) 72px 90px, var(--cyan) 90px 108px,
      var(--navy) 108px 126px, var(--purple) 126px 144px, var(--violet) 144px 162px,
      var(--red) 162px 180px, var(--yellow) 180px 198px, var(--orange) 198px 216px);
  }
  .bubble {
    position: absolute; border-radius: 50%;
    display: flex; flex-direction: column; align-items: center; justify-content: center;
    text-align: center; color: var(--ink-light);
    box-shadow: 3px 4px 8px rgba(0,0,0,.35);
  }
  .bubble h2 {
    font-family: "Fredoka", sans-serif; font-weight: 600; text-transform: lowercase;
    font-variant: small-caps; font-size: 25px; line-height: .95; letter-spacing: .5px;
    padding-bottom: 4px; margin-bottom: 6px; border-bottom: 2px solid var(--ink-light);
  }
  .bubble p { font-family: "Tinos", serif; font-size: 11px; line-height: 1.2; }
  .title { left: 2px; top: -32px; width: 300px; height: 300px; background: var(--c-title); z-index: 1; }
  .title h1 {
    font-family: "Fredoka", sans-serif; font-weight: 600; text-transform: lowercase;
    font-variant: small-caps; font-size: 32px; line-height: 1.15; letter-spacing: 1px;
    padding: 45px 0 0 12px;
  }
  .tip-one { left: 305px; top: 28px; width: 222px; height: 222px; background: var(--c-one); z-index: 1; }
  .tip-one p { width: 168px; }
  .tip-three { left: 377px; top: 240px; width: 238px; height: 238px; background: var(--c-three); z-index: 2; }
  .tip-three p { width: 196px; }
  .tip-two { left: 164px; top: 197px; width: 206px; height: 206px; background: var(--c-two); z-index: 3; }
  .tip-two p { width: 164px; }
  .tip-four { left: 13px; top: 368px; width: 208px; height: 208px; background: var(--c-four); z-index: 2; }
  .tip-four p { width: 172px; }
  .tip-six {
    left: 10px; top: 578px; width: 262px; height: 262px; background: var(--c-six); z-index: 3;
    justify-content: flex-start; padding-top: 20px;
  }
  .tip-six p { width: 186px; }
  .tip-five { left: 222px; top: 420px; width: 242px; height: 242px; background: var(--c-five); z-index: 4; }
  .tip-five p { width: 206px; }
  .good-luck { left: 423px; top: 575px; width: 220px; height: 220px; background: var(--c-luck); z-index: 5; }
  .good-luck h2 { font-size: 38px; text-transform: uppercase; font-variant: normal; }
  .good-luck p { width: 176px; }
  .footer-address {
    position: absolute; left: 21px; top: 832px;
    font-family: "Tinos", serif; font-size: 11.5px; line-height: 1.3; color: var(--footer-ink);
  }
  .brand {
    position: absolute; left: 372px; top: 826px; display: flex; align-items: center; gap: 8px;
    font-family: "Tinos", serif; font-weight: 700; color: var(--brand-ink);
  }
  .brand-dot { width: 34px; height: 34px; border-radius: 50%; background: var(--brand-ink); flex: none; }
  .brand-name { font-size: 15px; line-height: 1.05; text-transform: uppercase; }
</style>
</head>
<body>
<main class="poster">
  <div class="field">
    <section class="bubble title">
      <h1>How to get<br>organised<br>and motivated<br>this year.</h1>
    </section>

    <section class="bubble tip-one">
      <h2>1. Write<br>stuff down</h2>
      <p>Write down things you need to do and when you plan to do them. Use digital calendars, to do apps and email lists - or pen and paper. Even if you are sure you will remember - get it out of your head and onto paper/your phone/laptop. You are more likely to get it done and feel less stressed.</p>
    </section>

    <section class="bubble tip-two">
      <h2>2. Set up<br>your habits</h2>
      <p>If you do things in the same way, at the same time or after the same thing - then after a few weeks, it becomes much easier to get those things done. Set up a particular time, or place to do study tasks - or link them with another daily task. EG: art homework every Tuesday. Violin practice after breakfast.</p>
    </section>

    <section class="bubble tip-three">
      <h2>3. Focus</h2>
      <p>For 15-30 minutes at a time - totally focus on homework. Put your phone away, log out of chatterloop, close down other programs and really concentrate. Then have a break, send a text or whatever - and then go back to focussed study. Fifteen minutes of concentrated study gets more achieved than an hour of study switching back and forth between homework and other activities.</p>
    </section>

    <section class="bubble tip-four">
      <h2>4. Just do<br>something</h2>
      <p>No motivation? Just take a “bite”. Set a timer and just do 5 minutes. Or 15. Or read just the first two pages. Or the first problem on the worksheet. Something is better than nothing – and sometimes once you start, it’s easier to keep going.</p>
    </section>

    <section class="bubble tip-six">
      <h2>6. Imagine<br>the future</h2>
      <p>When you really can’t be find any motivation to do the things you need to do - take 30 seconds to think about what will happen in a week, month and year if you get on with it. What will happen then and how will that feel. And imagine what will happen in a week, month and year if you DON’T do those things - and how will that feel.</p>
    </section>

    <section class="bubble tip-five">
      <h2>5. Use<br>rewards and<br>consequences</h2>
      <p>Reward yourself when you do a hard task and use consequences when you don’t. Use food, fun activities, gaming and social time to motivate yourself - you get it when you do tasks, you don’t when you don’t. EG 15 minutes of clipstream when I finish this page. Tell other people your plans and you are more likely to stick to them.</p>
    </section>

    <section class="bubble good-luck">
      <h2>Good<br>luck!</h2>
      <p>For free articles and one to one help with study skills, increasing motivation, coping with stress or tough times in senior school, go to <strong>tallowbrook.example.net.au</strong> Tallow Brook Psychology and Education</p>
    </section>
  </div>

  <footer>
    <p class="footer-address">Suite 3/16 Larkspur Crescent, MERRIDALE,<br>5034 and 130-150 Fenwick Drive, ORCHARD VALE 5159<br>Phone : 08 5550 1711&nbsp; Fax: 08 5550 4055</p>
    <div class="brand">
      <span class="brand-dot"></span>
      <span class="brand-name">Tallow Brook<br>Psychology and Education</span>
    </div>
  </footer>
</main>
</body>
</html>
```